Flavour Wheel - Illustrator Graph

I need my basic layout, from the sample I provided, turned into a professional looking flavour wheel.

I have attached a sample of a final design I like, but please use your own creativity also.

All the exact words I need are on the uploaded illustration.

I would need the file supplied to me in .ai

Industry/Entity Type

Wheel

Font styles to use
Sans Serif

Colors

Designer to choose colors to be used in the design.

Requirements
Must have
• Files must be supplied in .ai format with fonts not outlined.
• I need each segment separated so I can change the colours if needed myself.
Nice to have
• I like small white gaps between the sections.

```html
<!DOCTYPE html>
<html lang="en">
<head>
<meta charset="utf-8">
<title>Flavour Wheel</title>
<link rel="stylesheet" href="https://fonts.googleapis.com/css2?family=Oswald:wght@400;500;600&display=swap">
<style>
  :root {
    --sour: #f4c430;
    --sour-soft: #fbe7a6;
    --sour-ink: #a9820a;
    --earthy: #6b9e3c;
    --earthy-soft: #d3e6bd;
    --earthy-ink: #4b7424;
    --sweet: #c4437f;
    --sweet-soft: #efc6d8;
    --sweet-ink: #9c2b5f;
    --salty: #7e98a4;
    --salty-soft: #d6e0e4;
    --salty-ink: #56707c;
    --savoury: #8d6b59;
    --savoury-soft: #e2d3ca;
    --savoury-ink: #6e4e3e;
    --spicy: #c9362f;
    --spicy-soft: #f2c7c3;
    --spicy-ink: #a3231d;
    --smoky: #d88c64;
    --smoky-soft: #f5d9ca;
    --smoky-ink: #a8603a;
    --ink: #1c1c1c;
    --rule: #dcdcdc;
    --paper: #ffffff;
  }
  html, body {
    margin: 0;
    padding: 0;
    width: 1200px;
    height: 1200px;
    overflow: hidden;
    background: var(--paper);
  }
  .flavour-wheel { display: block; width: 1200px; height: 1200px; }
  .segment path { stroke: var(--paper); stroke-width: 4; }

  .sour .outer, .sour .core { fill: var(--sour); }
  .sour .middle { fill: var(--sour-soft); }
  .earthy .outer, .earthy .core { fill: var(--earthy); }
  .earthy .middle { fill: var(--earthy-soft); }
  .sweet .outer, .sweet .core { fill: var(--sweet); }
  .sweet .middle { fill: var(--sweet-soft); }
  .salty .outer, .salty .core { fill: var(--salty); }
  .salty .middle { fill: var(--salty-soft); }
  .savoury .outer, .savoury .core { fill: var(--savoury); }
  .savoury .middle { fill: var(--savoury-soft); }
  .spicy .outer, .spicy .core { fill: var(--spicy); }
  .spicy .middle { fill: var(--spicy-soft); }
  .smoky .outer, .smoky .core { fill: var(--smoky); }
  .smoky .middle { fill: var(--smoky-soft); }

  .category-name {
    font-family: "Oswald", sans-serif;
    font-weight: 600;
    font-size: 22px;
    letter-spacing: 4px;
    fill: var(--paper);
    text-anchor: middle;
  }
  .sour-name { fill: var(--ink); }
  .descriptor {
    font-family: "Oswald", sans-serif;
    font-weight: 400;
    font-size: 18px;
    letter-spacing: 3px;
    fill: var(--ink);
    text-anchor: middle;
  }
  .hub-title {
    font-family: "Oswald", sans-serif;
    font-weight: 500;
    font-size: 19px;
    letter-spacing: 3px;
    fill: var(--ink);
    text-anchor: middle;
  }
  .tag text {
    font-family: "Oswald", sans-serif;
    font-size: 17px;
    letter-spacing: 2px;
  }
  .tag .inward { text-anchor: end; }
  .tags-sour circle { fill: var(--sour); } .tags-sour text { fill: var(--sour-ink); }
  .tags-earthy circle { fill: var(--earthy); } .tags-earthy text { fill: var(--earthy-ink); }
  .tags-sweet circle { fill: var(--sweet); } .tags-sweet text { fill: var(--sweet-ink); }
  .tags-salty circle { fill: var(--salty); } .tags-salty text { fill: var(--salty-ink); }
  .tags-savoury circle { fill: var(--savoury); } .tags-savoury text { fill: var(--savoury-ink); }
  .tags-spicy circle { fill: var(--spicy); } .tags-spicy text { fill: var(--spicy-ink); }
  .tags-smoky circle { fill: var(--smoky); } .tags-smoky text { fill: var(--smoky-ink); }
</style>
</head>
<body>
<svg class="flavour-wheel" viewBox="0 0 1500 1500" xmlns="http://www.w3.org/2000/svg">
  <defs>
    <path id="hub-path" d="M-88,0A88,88 0 1 1 88,0A88,88 0 1 1 -88,0"/>
  </defs>

  <g transform="translate(750,745)">
    <circle r="350" fill="none" stroke="var(--rule)" stroke-width="1.5"/>

    <g class="segment sour" transform="rotate(0)">
      <path class="outer" d="M0,-342A342,342 0 0 1 267.4,-213.2L215,-171.5A275,275 0 0 0 0,-275Z"/>
      <path class="middle" d="M0,-275A275,275 0 0 1 215,-171.5L117.3,-93.5A150,150 0 0 0 0,-150Z"/>
      <path class="core" d="M0,-150A150,150 0 0 1 117.3,-93.5L87.6,-69.8A112,112 0 0 0 0,-112Z"/>
    </g>
    <g class="segment earthy" transform="rotate(51.4286)">
      <path class="outer" d="M0,-342A342,342 0 0 1 267.4,-213.2L215,-171.5A275,275 0 0 0 0,-275Z"/>
      <path class="middle" d="M0,-275A275,275 0 0 1 215,-171.5L117.3,-93.5A150,150 0 0 0 0,-150Z"/>
      <path class="core" d="M0,-150A150,150 0 0 1 117.3,-93.5L87.6,-69.8A112,112 0 0 0 0,-112Z"/>
    </g>
    <g class="segment sweet" transform="rotate(102.857)">
      <path class="outer" d="M0,-342A342,342 0 0 1 267.4,-213.2L215,-171.5A275,275 0 0 0 0,-275Z"/>
      <path class="middle" d="M0,-275A275,275 0 0 1 215,-171.5L117.3,-93.5A150,150 0 0 0 0,-150Z"/>
      <path class="core" d="M0,-150A150,150 0 0 1 117.3,-93.5L87.6,-69.8A112,112 0 0 0 0,-112Z"/>
    </g>
    <g class="segment salty" transform="rotate(154.286)">
      <path class="outer" d="M0,-342A342,342 0 0 1 267.4,-213.2L215,-171.5A275,275 0 0 0 0,-275Z"/>
      <path class="middle" d="M0,-275A275,275 0 0 1 215,-171.5L117.3,-93.5A150,150 0 0 0 0,-150Z"/>
      <path class="core" d="M0,-150A150,150 0 0 1 117.3,-93.5L87.6,-69.8A112,112 0 0 0 0,-112Z"/>
    </g>
    <g class="segment savoury" transform="rotate(205.714)">
      <path class="outer" d="M0,-342A342,342 0 0 1 267.4,-213.2L215,-171.5A275,275 0 0 0 0,-275Z"/>
      <path class="middle" d="M0,-275A275,275 0 0 1 215,-171.5L117.3,-93.5A150,150 0 0 0 0,-150Z"/>
      <path class="core" d="M0,-150A150,150 0 0 1 117.3,-93.5L87.6,-69.8A112,112 0 0 0 0,-112Z"/>
    </g>
    <g class="segment spicy" transform="rotate(257.143)">
      <path class="outer" d="M0,-342A342,342 0 0 1 267.4,-213.2L215,-171.5A275,275 0 0 0 0,-275Z"/>
      <path class="middle" d="M0,-275A275,275 0 0 1 215,-171.5L117.3,-93.5A150,150 0 0 0 0,-150Z"/>
      <path class="core" d="M0,-150A150,150 0 0 1 117.3,-93.5L87.6,-69.8A112,112 0 0 0 0,-112Z"/>
    </g>
    <g class="segment smoky" transform="rotate(308.571)">
      <path class="outer" d="M0,-342A342,342 0 0 1 267.4,-213.2L215,-171.5A275,275 0 0 0 0,-275Z"/>
      <path class="middle" d="M0,-275A275,275 0 0 1 215,-171.5L117.3,-93.5A150,150 0 0 0 0,-150Z"/>
      <path class="core" d="M0,-150A150,150 0 0 1 117.3,-93.5L87.6,-69.8A112,112 0 0 0 0,-112Z"/>
    </g>

    <g transform="rotate(25.71)"><text class="category-name sour-name" y="-300">SOUR</text></g>
    <g transform="rotate(77.14)"><text class="category-name" y="-300">EARTHY</text></g>
    <g transform="rotate(128.57)"><text class="category-name" y="-300">SWEET</text></g>
    <g transform="rotate(180)"><text class="category-name" y="-300">SALTY</text></g>
    <g transform="rotate(231.43)"><text class="category-name" y="-300">SAVOURY</text></g>
    <g transform="rotate(282.86)"><text class="category-name" y="-300">SPICY</text></g>
    <g transform="rotate(334.29)"><text class="category-name" y="-300">SMOKY</text></g>

    <g transform="rotate(25.71)"><text class="descriptor"><tspan x="0" y="-228">BITTER</tspan><tspan x="0" y="-206">VINEGARY</tspan><tspan x="0" y="-184">CITRUS</tspan></text></g>
    <g transform="rotate(77.14)"><text class="descriptor"><tspan x="0" y="-228">FLORAL</tspan><tspan x="0" y="-206">HERVY</tspan><tspan x="0" y="-184">NUTTY</tspan></text></g>
    <g transform="rotate(128.57)"><text class="descriptor"><tspan x="0" y="-238">BUTTERY</tspan><tspan x="0" y="-216">FRUITY</tspan><tspan x="0" y="-194">SUGERY</tspan><tspan x="0" y="-172">CARAMEL</tspan></text></g>
    <g transform="rotate(180)"><text class="descriptor"><tspan x="0" y="-228">CHARRED</tspan><tspan x="0" y="-206">BRINEY</tspan></text></g>
    <g transform="rotate(231.43)"><text class="descriptor"><tspan x="0" y="-222">MEATINESS</tspan><tspan x="0" y="-200">UMAMI</tspan></text></g>
    <g transform="rotate(282.86)"><text class="descriptor"><tspan x="0" y="-228">CHILLI</tspan><tspan x="0" y="-206">PEPPERY</tspan><tspan x="0" y="-184">CAJUN</tspan></text></g>
    <g transform="rotate(334.29)"><text class="descriptor"><tspan x="0" y="-228">WOODY</tspan><tspan x="0" y="-206">FRUITY</tspan><tspan x="0" y="-184">ACRID</tspan></text></g>

    <g class="hub">
      <circle r="110" fill="var(--paper)"/>
      <circle r="66" fill="none" stroke="var(--rule)" stroke-width="2"/>
      <circle r="10" fill="var(--rule)"/>
      <text class="hub-title" dy="7"><textPath href="#hub-path" startOffset="138">FLAVOUR WHEEL</textPath></text>
      <text class="hub-title" dy="7"><textPath href="#hub-path" startOffset="415">FLAVOUR WHEEL</textPath></text>
    </g>

    <g class="tags-sour">
      <g class="tag" transform="rotate(-75.5)"><circle cx="365" r="6"/><text x="377" y="6">Rice Vinegar</text></g>
      <g class="tag" transform="rotate(-72)"><circle cx="365" r="6"/><text x="377" y="6">Balsamic Vinegar</text></g>
      <g class="tag" transform="rotate(-68.3)"><circle cx="365" r="6"/><text x="377" y="6">Apple Cider Vinegar</text></g>
      <g class="tag" transform="rotate(-61.3)"><circle cx="365" r="6"/><text x="377" y="6">Sumac</text></g>
      <g class="tag" transform="rotate(-57.7)"><circle cx="365" r="6"/><text x="377" y="6">Zests</text></g>
      <g class="tag" transform="rotate(-54.2)"><circle cx="365" r="6"/><text x="377" y="6">Lime</text></g>
      <g class="tag" transform="rotate(-50.6)"><circle cx="365" r="6"/><text x="377" y="6">Lemon</text></g>
    </g>

    <g class="tags-earthy">
      <g class="tag" transform="rotate(-41.9)"><circle cx="365" r="6"/><text x="377" y="6">Coriander</text></g>
      <g class="tag" transform="rotate(-38.3)"><circle cx="365" r="6"/><text x="377" y="6">Celery</text></g>
      <g class="tag" transform="rotate(-34.6)"><circle cx="365" r="6"/><text x="377" y="6">Tea</text></g>
      <g class="tag" transform="rotate(-30.9)"><circle cx="365" r="6"/><text x="377" y="6">Sage</text></g>
      <g class="tag" transform="rotate(-27.2)"><circle cx="365" r="6"/><text x="377" y="6">Oregano</text></g>
      <g class="tag" transform="rotate(-23.4)"><circle cx="365" r="6"/><text x="377" y="6">Thyme</text></g>
      <g class="tag" transform="rotate(-19.7)"><circle cx="365" r="6"/><text x="377" y="6">Rosemary</text></g>
      <g class="tag" transform="rotate(-15.9)"><circle cx="365" r="6"/><text x="377" y="6">Bay Leaf</text></g>
      <g class="tag" transform="rotate(-12.4)"><circle cx="365" r="6"/><text x="377" y="6">Fennel</text></g>
      <g class="tag" transform="rotate(-8.7)"><circle cx="365" r="6"/><text x="377" y="6">Five Spice Nutmeg</text></g>
      <g class="tag" transform="rotate(-5)"><circle cx="365" r="6"/><text x="377" y="6">Tumeric</text></g>
      <g class="tag" transform="rotate(-1.3)"><circle cx="365" r="6"/><text x="377" y="6">Star Anise</text></g>
      <g class="tag" transform="rotate(2.4)"><circle cx="365" r="6"/><text x="377" y="6">Cinnamon</text></g>
      <g class="tag" transform="rotate(6.3)"><circle cx="365" r="6"/><text x="377" y="6">Clove</text></g>
      <g class="tag" transform="rotate(10)"><circle cx="365" r="6"/><text x="377" y="6">Pecan</text></g>
      <g class="tag" transform="rotate(13.5)"><circle cx="365" r="6"/><text x="377" y="6">Coffee</text></g>
    </g>

    <g class="tags-sweet">
      <g class="tag" transform="rotate(19.6)"><circle cx="365" r="6"/><text x="377" y="6">BUTTER</text></g>
      <g class="tag" transform="rotate(23.2)"><circle cx="365" r="6"/><text x="377" y="6">FRUIT JUICE</text></g>
      <g class="tag" transform="rotate(27)"><circle cx="365" r="6"/><text x="377" y="6">FRUITS</text></g>
      <g class="tag" transform="rotate(30.8)"><circle cx="365" r="6"/><text x="377" y="6">SAUCE/KETCHUP</text></g>
      <g class="tag" transform="rotate(38)"><circle cx="365" r="6"/><text x="377" y="6">COLA</text></g>
      <g class="tag" transform="rotate(41.8)"><circle cx="365" r="6"/><text x="377" y="6">AGAVE NECTAR</text></g>
      <g class="tag" transform="rotate(45.6)"><circle cx="365" r="6"/><text x="377" y="6">SUGARS</text></g>
      <g class="tag" transform="rotate(52.9)"><circle cx="365" r="6"/><text x="377" y="6">HONEY</text></g>
      <g class="tag" transform="rotate(56.7)"><circle cx="365" r="6"/><text x="377" y="6">MOLASSES</text></g>
      <g class="tag" transform="rotate(60.6)"><circle cx="365" r="6"/><text x="377" y="6">MAPLE SYRUP</text></g>
    </g>

    <g class="tags-salty">
      <g class="tag" transform="rotate(73.2)"><circle cx="365" r="6"/><text x="377" y="6">ANCHOVIES</text></g>
      <g class="tag" transform="rotate(77)"><circle cx="365" r="6"/><text x="377" y="6">GARLIC</text></g>
      <g class="tag" transform="rotate(80.8)"><circle cx="365" r="6"/><text x="377" y="6">SEA SALT</text></g>
      <g class="tag" transform="rotate(84.5)"><circle cx="365" r="6"/><text x="377" y="6">KOSHER SALT</text></g>
      <g class="tag" transform="rotate(91.4)"><circle cx="365" r="6"/><text x="377" y="6">SOY SAUCE</text></g>
      <g class="tag" transform="rotate(95.4)"><circle cx="365" r="6"/><text x="377" y="6">FISH SAUCE</text></g>
      <g class="tag" transform="rotate(99)"><circle cx="365" r="6"/><text x="377" y="6">WORCESTERSHIR SAUCE</text></g>
      <g class="tag" transform="rotate(102.4)"><circle cx="365" r="6"/><text x="377" y="6">SEASONING SAUCE</text></g>
    </g>

    <g class="tags-savoury">
      <g class="tag" transform="rotate(329)"><circle cx="-365" r="6"/><text class="inward" x="-377" y="6">MSG</text></g>
      <g class="tag" transform="rotate(325.5)"><circle cx="-365" r="6"/><text class="inward" x="-377" y="6">VEGESPREAD</text></g>
      <g class="tag" transform="rotate(322)"><circle cx="-365" r="6"/><text class="inward" x="-377" y="6">LARD</text></g>
      <g class="tag" transform="rotate(318.4)"><circle cx="-365" r="6"/><text class="inward" x="-377" y="6">STOCKS</text></g>
      <g class="tag" transform="rotate(315)"><circle cx="-365" r="6"/><text class="inward" x="-377" y="6">PHOSPHATES</text></g>
    </g>

    <g class="tags-spicy">
      <g class="tag" transform="rotate(341.5)"><circle cx="-365" r="6"/><text class="inward" x="-377" y="6">HORSERADISH</text></g>
      <g class="tag" transform="rotate(345.2)"><circle cx="-365" r="6"/><text class="inward" x="-377" y="6">WASABI</text></g>
      <g class="tag" transform="rotate(349)"><circle cx="-365" r="6"/><text class="inward" x="-377" y="6">PEPPER</text></g>
      <g class="tag" transform="rotate(352.6)"><circle cx="-365" r="6"/><text class="inward" x="-377" y="6">CUMIN</text></g>
      <g class="tag" transform="rotate(356.2)"><circle cx="-365" r="6"/><text class="inward" x="-377" y="6">ALLSPICE</text></g>
      <g class="tag" transform="rotate(360)"><circle cx="-365" r="6"/><text class="inward" x="-377" y="6">SZECHUAN</text></g>
      <g class="tag" transform="rotate(363.8)"><circle cx="-365" r="6"/><text class="inward" x="-377" y="6">ONION</text></g>
      <g class="tag" transform="rotate(370.9)"><circle cx="-365" r="6"/><text class="inward" x="-377" y="6">CHIPOTLE</text></g>
      <g class="tag" transform="rotate(374.9)"><circle cx="-365" r="6"/><text class="inward" x="-377" y="6">JALAPENO</text></g>
      <g class="tag" transform="rotate(378.3)"><circle cx="-365" r="6"/><text class="inward" x="-377" y="6">HOT SAUCE</text></g>
      <g class="tag" transform="rotate(382.2)"><circle cx="-365" r="6"/><text class="inward" x="-377" y="6">HABANERO</text></g>
      <g class="tag" transform="rotate(385.7)"><circle cx="-365" r="6"/><text class="inward" x="-377" y="6">RED PEPPER</text></g>
      <g class="tag" transform="rotate(389.5)"><circle cx="-365" r="6"/><text class="inward" x="-377" y="6">MUSTARD</text></g>
      <g class="tag" transform="rotate(393.3)"><circle cx="-365" r="6"/><text class="inward" x="-377" y="6">PAPRIKA</text></g>
    </g>

    <g class="tags-smoky">
      <g class="tag" transform="rotate(402.5)"><circle cx="-365" r="6"/><text class="inward" x="-377" y="6">HARD WOODS</text></g>
      <g class="tag" transform="rotate(406.2)"><circle cx="-365" r="6"/><text class="inward" x="-377" y="6">FRUIT WOODS</text></g>
      <g class="tag" transform="rotate(409.8)"><circle cx="-365" r="6"/><text class="inward" x="-377" y="6">CHARCOAL</text></g>
      <g class="tag" transform="rotate(413.2)"><circle cx="-365" r="6"/><text class="inward" x="-377" y="6">WHISKEY</text></g>
      <g class="tag" transform="rotate(417)"><circle cx="-365" r="6"/><text class="inward" x="-377" y="6">BOURBON</text></g>
      <g class="tag" transform="rotate(424.3)"><circle cx="-365" r="6"/><text class="inward" x="-377" y="6">CREOSOTE</text></g>
      <g class="tag" transform="rotate(431.7)"><circle cx="-365" r="6"/><text class="inward" x="-377" y="6">COCKTAIL BITTERS</text></g>
      <g class="tag" transform="rotate(435.1)"><circle cx="-365" r="6"/><text class="inward" x="-377" y="6">CIRBIC ACID</text></g>
      <g class="tag" transform="rotate(442.6)"><circle cx="-365" r="6"/><text class="inward" x="-377" y="6">TAMARIND</text></g>
    </g>
  </g>
</svg>
</body>
</html>
```